Professional Business Cards

We need a nice looking, profession and modern business card for our new company. Our logo is attatched

Target Market(s)

Young Professionals

Industry/Entity Type

Financial

Contact Information for Business Card

FRONT

Vardane Ledger Pty Ltd
Level 22, Harbour Point, 48 Wattlebrook Ave
Sydney NSW 2000
ABN : 47 318 905 226

Owen Hadley - Chief Operations Officer
P : 02 9173 5528
M: 0418 356 091
owen@vardaneledger,com

BACK

- Cryptocurrency Exchange Services
- Cryptocurrency Mining Operations
- Cryptocurrency Investment Fund Offering

Font styles to use
Sans Serif

Colors
0255a3
9d9d9d

```html
<!DOCTYPE html>
<html lang="en">
<head>
<meta charset="utf-8">
<title>Vardane Ledger Business Cards</title>
<link rel="stylesheet" href="https://fonts.googleapis.com/css2?family=Questrial&display=swap">
<style>
  :root {
    --brand-blue: #0255a3;
    --brand-grey: #9d9d9d;
    --ink: #4a4a4a;
    --card-dark: #2a2a2b;
    --card-light: #ffffff;
    --backdrop: #e4e4e6;
    --rule: #8a8a8a;
    --service-text: #d6d6d6;
  }
  * { box-sizing: border-box; margin: 0; padding: 0; }
  html, body { width: 1200px; height: 834px; overflow: hidden; }
  body {
    background: var(--backdrop);
    font-family: "Questrial", "Century Gothic", sans-serif;
    display: flex;
    align-items: center;
    justify-content: center;
    gap: 40px;
  }
  .card {
    width: 540px;
    height: 310px;
    position: relative;
    box-shadow: 0 6px 18px rgba(0,0,0,.18);
  }
  .wordmark {
    display: flex;
    align-items: center;
    gap: 10px;
    color: var(--brand-blue);
    font-size: 30px;
    letter-spacing: 1px;
    text-transform: uppercase;
    white-space: nowrap;
  }
  .wordmark-square {
    width: 22px; height: 22px;
    background: var(--brand-blue);
  }

  /* back */
  .card-back {
    background: var(--card-dark);
    display: flex;
    flex-direction: column;
    align-items: center;
    justify-content: center;
    gap: 34px;
  }
  .services {
    color: var(--service-text);
    font-size: 12.5px;
    text-align: center;
    line-height: 1.7;
    letter-spacing: .2px;
  }

  /* front */
  .card-front { background: var(--card-light); }
  .card-front .wordmark { position: absolute; left: 38px; top: 52px; font-size: 28px; }
  .person {
    position: absolute; right: 36px; top: 48px; text-align: right;
  }
  .person-name { color: var(--ink); font-size: 19px; letter-spacing: .3px; }
  .person-title { color: var(--brand-blue); font-size: 12.5px; margin-top: 3px; }
  .rule-top {
    position: absolute; right: 36px; top: 98px; width: 300px;
    border-top: 1px solid var(--rule);
  }
  .contacts {
    position: absolute; right: 36px; top: 110px;
    list-style: none; text-align: right;
    color: var(--ink); font-size: 12px; line-height: 20px;
  }
  .contacts li { display: flex; align-items: center; justify-content: flex-end; gap: 8px; }
  .contacts svg { width: 13px; height: 13px; stroke: var(--brand-blue); fill: none; stroke-width: 1.4; }
  .rule-bottom {
    position: absolute; left: 38px; top: 212px; width: 230px;
    border-top: 1px solid var(--rule);
  }
  .company {
    position: absolute; left: 38px; top: 222px;
    font-style: normal; color: var(--ink); font-size: 12px; line-height: 17px;
  }
  .company-name { color: var(--brand-blue); font-size: 12.5px; }
</style>
</head>
<body>
  <section class="card card-back" aria-label="Card back">
    <div class="wordmark"><span class="wordmark-square"></span>Vardane Ledger</div>
    <p class="services">
      Cryptocurrency Exchange Services &nbsp;|&nbsp; Cryptocurrency Mining Operations<br>
      Cryptocurrency Investment Fund Offering
    </p>
  </section>

  <section class="card card-front" aria-label="Card front">
    <div class="wordmark"><span class="wordmark-square"></span>Vardane Ledger</div>

    <div class="person">
      <p class="person-name">Owen Hadley</p>
      <p class="person-title">Chief Operations Officer</p>
    </div>
    <div class="rule-top"></div>
    <ul class="contacts">
      <li>02 9173 5528
        <svg viewBox="0 0 14 14"><path d="M3 1.5l2 .5 1 3-1.5 1a7 7 0 0 0 3.5 3.5l1-1.5 3 1 .5 2-1.5 1.5C6 12 2 8 1.5 3z"/></svg>
      </li>
      <li>0418 356 091
        <svg viewBox="0 0 14 14"><rect x="4" y="1.5" width="6" height="11" rx="1"/><path d="M6.3 10.5h1.4"/></svg>
      </li>
      <li>owen@vardaneledger,com
        <svg viewBox="0 0 14 14"><rect x="1.5" y="3" width="11" height="8"/><path d="M1.5 3l5.5 4.5L12.5 3"/></svg>
      </li>
    </ul>

    <div class="rule-bottom"></div>
    <address class="company">
      <span class="company-name">Vardane Ledger Pty Ltd</span><br>
      Level 22, Harbour Point, 48 Wattlebrook Ave<br>
      Sydney NSW 2000
    </address>
  </section>
</body>
</html>
```